Business cards for Wheelnest

We need a business card layout for our new bike and e-bike rental (we also sell used e-bikes and bike accessories). The logo already exists.

```html
<!DOCTYPE html>
<html lang="en">
<head>
<meta charset="utf-8">
<title>Wheelnest – Business Cards</title>
<link rel="stylesheet" href="https://fonts.googleapis.com/css2?family=Encode+Sans+Semi+Condensed:wght@300&family=Open+Sans:wght@700&family=Zilla+Slab:wght@400&display=swap">
<style>
  :root {
    --bg: #2a2c2f;
    --card-dark: #1d3337;
    --card-dark-deep: #172a2d;
    --mint: #5cc6a8;
    --white: #f2f5f4;
    --text-soft: #d7dedd;
  }
  * { margin: 0; padding: 0; box-sizing: border-box; }
  html, body { width: 1200px; height: 900px; overflow: hidden; }
  body {
    background: var(--bg);
    position: relative;
  }
  .card {
    position: absolute;
    border-radius: 26px;
    overflow: hidden;
    background: linear-gradient(160deg, var(--card-dark) 0%, var(--card-dark-deep) 100%);
    box-shadow: 0 18px 40px rgba(0,0,0,.45);
  }

  /* Contact card (portrait) */
  .card-contact {
    left: 130px; top: 140px;
    width: 360px; height: 620px;
  }
  .card-contact .panel {
    position: absolute; inset: 0;
  }
  .card-contact .panel-name {
    position: absolute;
    left: 40px; right: 0; top: 150px;
    text-align: center;
    font-family: "Encode Sans Semi Condensed", sans-serif;
    font-weight: 300;
    font-size: 44px;
    letter-spacing: 1px;
    color: var(--card-dark);
  }
  .contact {
    position: absolute;
    left: 48px; top: 380px;
    right: 30px;
  }
  .contact .person {
    font-family: "Encode Sans Semi Condensed", sans-serif;
    font-weight: 300;
    font-size: 26px;
    letter-spacing: .5px;
    color: var(--mint);
    text-transform: uppercase;
  }
  .contact .role {
    font-family: "Zilla Slab", serif;
    font-size: 19px;
    color: var(--text-soft);
    margin-top: 2px;
  }
  .contact .rule {
    width: 14px; height: 2px;
    background: var(--mint);
    margin: 18px 0 18px;
  }
  .contact ul { list-style: none; }
  .contact li {
    display: flex; align-items: center; gap: 14px;
    font-family: "Zilla Slab", serif;
    font-size: 19px;
    color: var(--text-soft);
    line-height: 1;
    margin-bottom: 12px;
  }
  .contact li svg { width: 16px; height: 16px; flex: none; }

  /* Brand card (landscape) */
  .card-brand {
    left: 540px; top: 270px;
    width: 620px; height: 360px;
  }
  .brand-name {
    position: absolute;
    left: 70px; top: 118px;
    font-family: "Encode Sans Semi Condensed", sans-serif;
    font-weight: 300;
    font-size: 82px;
    letter-spacing: 2px;
    color: var(--mint);
    line-height: 1;
  }
  .brand-dot {
    position: absolute;
    left: 486px; top: 66px;
    width: 30px; height: 30px;
    border-radius: 50%;
    background: var(--mint);
  }
  .tagline {
    position: absolute;
    left: 74px; top: 222px;
    font-family: "Open Sans", sans-serif;
    font-weight: 700;
    font-size: 24px;
    color: var(--white);
  }
</style>
</head>
<body>

<section class="card card-contact" aria-label="Business card, contact side">
  <svg class="panel" viewBox="0 0 360 620" aria-hidden="true">
    <path fill="var(--mint)" d="M70 26 H360 V330 H70 V310 H40 V56 H70 Z"/>
  </svg>
  <div class="panel-name">Wheelnest</div>

  <div class="contact">
    <div class="person">Marlon Reed</div>
    <div class="role">Owner</div>
    <div class="rule"></div>
    <ul>
      <li>
        <svg viewBox="0 0 16 16" aria-hidden="true"><path fill="var(--mint)" d="M3 2h3l1.5 3.5-2 1.2a9 9 0 0 0 3.8 3.8l1.2-2L14 10v3a1 1 0 0 1-1 1A11 11 0 0 1 2 3a1 1 0 0 1 1-1z"/></svg>
        012 555 0147
      </li>
      <li>
        <svg viewBox="0 0 16 16" aria-hidden="true"><rect x="1" y="3" width="14" height="10" rx="1" fill="var(--mint)"/><path d="M1.5 3.8 8 9l6.5-5.2" fill="none" stroke="var(--card-dark)" stroke-width="1.3"/></svg>
        hello@Wheelnest.com
      </li>
      <li>
        <svg viewBox="0 0 16 16" aria-hidden="true"><circle cx="8" cy="8" r="7" fill="var(--mint)"/><path d="M1 8h14M8 1c-3 3.5-3 10.5 0 14M8 1c3 3.5 3 10.5 0 14" fill="none" stroke="var(--card-dark)" stroke-width="1"/></svg>
        Wheelnest.com
      </li>
    </ul>
  </div>
</section>

<section class="card card-brand" aria-label="Business card, brand side">
  <span class="brand-dot" aria-hidden="true"></span>
  <div class="brand-name">WHEELNEST</div>
  <div class="tagline">simply e-ride away</div>
</section>

</body>
</html>
```